Copperleaf Grill
there is none
Copperleaf Grill -
Simple
Danielle Whitcomb
Proprietor
318 Ferrand Street New Orleans, LA 70119
dwhitcomb@copperleaf-eats.com
www.copperleaf-eats.com
Use the same font of Grill and New Orleans for information on card
Just put the logo and website on the back of the card

```html
<!DOCTYPE html>
<html lang="en">
<head>
<meta charset="utf-8">
<title>Copperleaf Grill – Business Card</title>
<link href="https://fonts.googleapis.com/css2?family=Cabin:wght@400;600&display=swap" rel="stylesheet">
<style>
  :root {
    --wine: #8b2433;
    --ink: #2b2b2b;
    --paper: #ffffff;
    --edge: #9a9a9a;
    --page: #ffffff;
  }
  * { margin: 0; padding: 0; box-sizing: border-box; }
  html, body {
    width: 1200px; height: 929px; overflow: hidden;
    background: var(--page);
    font-family: "Cabin", "Gill Sans", sans-serif;
  }
  .canvas { position: relative; width: 1200px; height: 929px; }
  .card {
    position: absolute; top: 314px;
    width: 368px; height: 212px;
    background: var(--paper);
    border: 1px solid var(--edge);
    border-radius: 14px;
    overflow: hidden;
  }
  .card--front { left: 168px; }
  .card--back { left: 602px; }

  .front__band {
    position: absolute; left: 0; top: 0; bottom: 0; width: 132px;
    background: var(--wine);
  }
  .holder { position: absolute; left: 12px; top: 34px; color: var(--paper); }
  .holder__name { font-size: 11.5px; font-weight: 600; letter-spacing: 0.3px; text-transform: uppercase; }
  .holder__title { font-size: 7px; margin-top: 1px; }

  .brand {
    display: flex; align-items: center; gap: 6px;
    position: absolute; color: var(--ink);
    font-size: 21px; font-weight: 400; white-space: nowrap;
  }
  .brand__dot { width: 9px; height: 9px; border-radius: 50%; background: var(--wine); flex: none; }
  .card--front .brand { left: 152px; top: 68px; }
  .card--back .brand { left: 50%; top: 86px; transform: translateX(-50%); }

  .contact {
    position: absolute; left: 173px; top: 130px;
    font-size: 7.6px; line-height: 1.32; color: var(--ink);
  }
  .contact__gap { height: 8px; }

  .back__band {
    position: absolute; left: 0; right: 0; bottom: 0; height: 28px;
    background: var(--wine);
    color: var(--paper); font-size: 8.5px;
    display: flex; align-items: center; justify-content: flex-end;
    padding-right: 16px;
  }
</style>
</head>
<body>
<div class="canvas">
  <section class="card card--front">
    <div class="front__band"></div>
    <div class="holder">
      <p class="holder__name">Danielle Whitcomb</p>
      <p class="holder__title">Proprietor</p>
    </div>
    <div class="brand"><span class="brand__dot"></span>Copperleaf Grill</div>
    <div class="contact">
      <p>318 Ferrand Street</p>
      <p>New Orleans, LA 70119</p>
      <div class="contact__gap"></div>
      <p>Phone: 504.555.0142</p>
      <p>Cell: 504.555.0187</p>
      <p>Email: dwhitcomb@copperleaf-eats.com</p>
    </div>
  </section>

  <section class="card card--back">
    <div class="brand"><span class="brand__dot"></span>Copperleaf Grill</div>
    <div class="back__band">Web: www.copperleaf-eats.com</div>
  </section>
</div>
</body>
</html>
```